San Francisco Leading Consulting firm - 47Nova Web Design Project

•Create a Web Design
•Uncoded webpage layout design
•2 Pages Design - Homepage + Interior Page

Task Description
Hello, we're looking for a re-design our current website www.47nova-example.com

we have a sample mockup design @

http://47nova.civicpane-example.org/

This shows the layout that we like and also a sample of 6 pictures that would change based on where you mouse over..

6 pictures HOME design needs to be included.

SMART
THOUGHTFUL
FLEXIBLE
CREATIVE SERVICES
TECHNICAL SERVICES
PARTNERS

sites we like:

http://www.brelmoradvisory-example.com/Home.cfm?id=Home
http://www.pixelquarry-example.com/index.html

Our company can be best described as: 100+ employees, cutting-edge, depandable, innovative, strong, smart.

Our Primary focus is: IT Consulting Services and Creative Design services

47Nova LLC is a consulting firm providing creative design, business and technology solutions to both private and public interests.

Established in 1996, 47Nova is a San Francisco based company providing specialists for a range of business needs including:

Creative Design Services
•Print
•Logo Design
•Website Design
•Illustration

and

Business and Technology solutions

•Application Software and Web Development
•Business Process Re-Design (BPR)
•Business/Systems Analysis and Requirement Documentation
•Mentoring and Training
•Network/Hardware Installation Services
•System Design and Architecture
•Vendor Management
•Teamvault Architecture and Implementation

our sample mockup site:

Reason: Due to holiday season, we're not available to work with designers and finilize our design.  

Thank you very much for submitting your design.

We appreciate your time and creativity.   Since, our office is currently closed for holidays, we will be reviewing it in details next week and will make our decision as soon as possible.

It would be great if you could submit any of your changes by Wed next week, so it would be part of our reviews. 

Please see updated wireframe under attachments:  we have some minor updates to our wireframe that we would like you to update your designs, if possible.  

We also encorouge you not to use our standard wireframe and come up with more unique designs.   Everything would be considered when we review your design.

 

Target Market(s)

Creative services and professional services clients, including government agencies

Industry/Entity Type

Business

Requirements
Must have
• Clean, professional look, easy navigation

```html
<!DOCTYPE html>
<html lang="en">
<head>
<meta charset="utf-8">
<title>47Nova – Corelith Web Applications</title>
<link rel="stylesheet" href="https://fonts.googleapis.com/css2?family=PT+Sans:ital,wght@0,400;0,700;1,400&family=Open+Sans:wght@400;600&display=swap">
<style>
:root{
  --brand-blue:#0a7dbd;
  --nav-blue:#0b78b8;
  --nav-active:#2b3640;
  --ink:#1f1f1f;
  --muted:#9a9a9a;
  --rule:#cfcfcf;
  --topbar:#111;
  --footer-top:#3c3c3c;
  --footer-bottom:#050505;
  --white:#fff;
}
*{box-sizing:border-box;margin:0;padding:0}
html,body{width:1200px;height:1108px;overflow:hidden;background:var(--white)}
body{position:relative;font-family:"Open Sans",sans-serif;color:var(--ink)}
.topbar{position:absolute;left:0;top:0;width:1200px;height:25px;background:linear-gradient(#2a2a2a,var(--topbar));}
.login{position:absolute;right:170px;top:4px;display:flex;align-items:center;gap:6px;font-family:"PT Sans",sans-serif;font-size:11px;font-weight:700;color:var(--white)}
.login .field{width:115px;height:16px;background:var(--white);color:#333;font-weight:400;font-size:10px;padding:1px 4px;line-height:14px}
.login .go{margin-left:10px}
.logo{position:absolute;left:160px;top:60px;display:flex;align-items:center;gap:14px}
.logo .dot{width:60px;height:60px;border-radius:50%;background:var(--brand-blue)}
.logo .name{font-family:"PT Sans",sans-serif;font-size:54px;color:#333;letter-spacing:1px}
.address{position:absolute;right:175px;top:58px;text-align:right;font-size:11.5px;line-height:13.5px;color:var(--muted)}
.address .gap{height:13px}
.nav{position:absolute;left:156px;top:179px;width:887px;height:41px;background:var(--nav-blue);display:flex}
.nav a{flex:1;display:flex;align-items:center;justify-content:center;color:var(--white);text-decoration:none;font-family:"PT Sans",sans-serif;font-size:17px;border-right:1px solid #2a8ccb}
.nav a:last-child{border-right:none}
.nav a.active{color:var(--nav-active)}
.content{position:absolute;left:166px;top:252px;width:610px}
.content h1{font-weight:400;font-size:23px;color:var(--brand-blue);margin-bottom:12px}
.content p{font-size:11.6px;line-height:12.8px;margin-left:9px;width:594px;text-align:justify}
.content h2{font-weight:400;font-size:13.5px;margin:50px 0 2px 9px}
.content .cta{margin-top:86px;text-align:left}
.content .cta a{color:var(--brand-blue);text-decoration:none}
.divider{position:absolute;left:789px;top:256px;width:1px;height:609px;background:var(--rule)}
.sidenav{position:absolute;left:794px;top:264px;width:232px;list-style:none}
.sidenav li{height:27.7px;border-bottom:1px solid var(--rule);padding-left:13px;display:flex;align-items:center;font-family:"PT Sans",sans-serif;font-size:14.5px;color:#222}
.sidenav li.current{color:var(--brand-blue)}
.footer{position:absolute;left:0;top:912px;width:1200px;height:196px;background:linear-gradient(var(--footer-top),var(--footer-bottom) 60%);border-top:2px solid #aaa}
.col{position:absolute;top:8px;width:232px}
.col h3{font-family:"PT Sans",sans-serif;font-style:italic;font-weight:400;font-size:16px;color:var(--white);padding:0 0 6px 26px;border-bottom:1px solid #555}
.col ul{list-style:none;padding:8px 0 0 20px}
.col li{font-size:11.5px;color:var(--white);line-height:22px}
.col-follow{left:191px}
.col-company{left:492px}
.col-links{left:778px}
.social{display:grid;grid-template-columns:repeat(3,27px);gap:9px 9px;padding:8px 0 0 7px}
.social span{width:27px;height:27px;border-radius:3px;background:#e9eef2;border:2px solid #fff}
.copyright{position:absolute;left:0;top:162px;width:1200px;text-align:center;font-size:11.5px;color:var(--white)}
</style>
</head>
<body>
<header class="topbar">
  <div class="login"><span>Client Login</span><span class="field">username</span><span class="field">password</span><span class="go">GO</span></div>
</header>
<div class="logo"><span class="dot"></span><span class="name">47Nova</span></div>
<address class="address" style="font-style:normal">
  47Nova, LLC<br>2274 Harlow Street, Suite 880<br>San Francisco, CA 94199
  <div class="gap"></div>
  Phone: 1-415-555-0142<br>Fax: 1-415-555-0147
</address>
<nav class="nav">
  <a href="#">Our Company</a><a href="#" class="active">Technical Services</a><a href="#">Creative Services</a><a href="#">Our Partners</a><a href="#">Contact Us</a>
</nav>
<main class="content">
  <h1>Corelith Web Applications</h1>
  <p>Lorem ipsum dolor sit amet, consectetur adipiscing elit. Suspendisse diam magna, aliquet non pulvinar adipiscing, sagittis ut diam. Phasellus volutpat, dui eget elementum semper, lectus eros iaculis mauris, a convallis elit ante non diam. Aenean euismod, justo vitae lobortis ultrices, sem felis placerat lacus, non iaculis eros magna nec tellus. Praesent accumsan convallis tellus non porta. Quisque in velit vitae ipsum semper tincidunt ut venenatis est. Sed rhoncus orci eu sem malesuada pulvinar. Praesent id justo velit, vel tempus ante. Donec feugiat augue eget sapien blandit eu tristique sem fringilla. Class aptent taciti sociosqu ad litora torquent per conubia nostra, per inceptos himenaeos.</p>
  <h2>Custom CorePage Application Development</h2>
  <p>Lorem ipsum dolor sit amet, consectetur adipiscing elit. Suspendisse diam magna, aliquet non pulvinar adipiscing, sagittis ut diam. Phasellus volutpat, dui eget elementum semper, lectus eros iaculis mauris, a convallis elit ante non diam. Aenean euismod, justo vitae lobortis ultrices, sem felis placerat lacus, non iaculis eros magna nec tellus. Praesent accumsan convallis tellus non porta. Quisque in velit vitae ipsum semper tincidunt ut venenatis est. Sed rhoncus orci eu sem malesuada pulvinar. Praesent id justo velit, vel tempus ante. Donec feugiat augue eget sapien blandit eu tristique sem fringilla. Class aptent taciti sociosqu ad litora torquent per conubia nostra, per inceptos himenaeos.</p>
  <h2>Corelith E-commerce Programming</h2>
  <p>Lorem ipsum dolor sit amet, consectetur adipiscing elit. Suspendisse diam magna, aliquet non pulvinar adipiscing, sagittis ut diam. Phasellus volutpat, dui eget elementum semper, lectus eros iaculis mauris, a convallis elit ante non diam. Aenean euismod, justo vitae lobortis ultrices, sem felis placerat lacus, non iaculis eros magna nec tellus. Praesent accumsan convallis tellus non porta. Quisque in velit vitae ipsum semper tincidunt ut venenatis est. Sed rhoncus orci eu sem malesuada pulvinar. Praesent id justo velit, vel tempus ante. Donec feugiat augue eget sapien blandit eu tristique sem fringilla. Class aptent taciti sociosqu ad litora torquent per conubia nostra, per inceptos himenaeos.</p>
  <p class="cta"><a href="#">Contact us</a> today to find out more about how we can help you with your Corelith and CorePage application development needs.</p>
</main>
<div class="divider"></div>
<ul class="sidenav">
  <li>Business Intelligence Consulting</li>
  <li>Teamvault Consulting</li>
  <li>EDI SOA Consulting</li>
  <li class="current">Corelith Web Applications</li>
  <li>Dashboards Reports</li>
  <li>Document Management</li>
  <li>Marketing Collateral</li>
  <li>Packaging</li>
  <li>Books</li>
</ul>
<footer class="footer">
  <div class="col col-follow">
    <h3>Follow Us</h3>
    <div class="social" role="img" aria-label="Social network links">
      <span></span><span></span><span></span><span></span><span></span><span></span>
    </div>
  </div>
  <div class="col col-company">
    <h3>Company</h3>
    <ul><li>Sitemap</li><li>Support</li><li>Contact Us</li><li>Privacy Policy</li></ul>
  </div>
  <div class="col col-links">
    <h3>Related Links</h3>
    <ul><li>Related Link 1</li><li>Related Link 2</li><li>Related Link 3</li><li>Related Link 4</li></ul>
  </div>
  <p class="copyright">Copyright 2010, 47Nova, LLC All rights reserved</p>
</footer>
</body>
</html>
```